Popcorn, ice cream, alcohol infused shakes shop

Create a clean simple website with pictures and bold type for a popcorn, ice cream and boozy shake shop. The site should have:
- Unique and Large Typography
- Large & Responsive Hero (stunning, elicits a response) Images.No concern with above or below the fold. Create a strong visual experience that encourages visitors to scroll down to read more. Use large images to visually tell a story without having to rely on just text.
- Flat image designs
- Place for me to upload an ad type video
- Hidden type menu (three line menu)
- A few small card like images (food, gift bags, tins, etc.) menu items with a brief description.

Target Market(s)

21-49 years of age for the boozy shakes. Soccer moms for sports teams & sleepovers, professionals (teachers, realtors, pharm sales), gifts for family and friends. Also some kids

Coding

Coded - Design and coding required

Number of Pages Required

5+ page

Font styles to use
Sans Serif

Colors

Designer to choose colors to be used in the design.

Requirements
Must have
• Images of gourmet popcorn, fancy shakes, ice cream, gift bags and popcorn tins. Holiday popcorn tins and gift bags along with grift certificates. Ability for visitors to send a contact form to rt@fizzlane.net
• Five pages - Home Page, AboutUs, Menu, Gift/Promotion, Contact Us
Nice to have
• Smooth flow on the home page. Mostly images and bold text.
Should not have
• Too many words. Boring text fonts

```html
<!DOCTYPE html>
<html lang="en">
<head>
<meta charset="utf-8">
<title>Pop Parlor — Popcorn, Ice Cream & Boozy Shakes</title>
<link href="https://fonts.googleapis.com/css2?family=Bebas+Neue&family=Lobster&family=Montserrat:wght@400;500;600;700;900&family=Prata&display=swap" rel="stylesheet">
<style>
:root{
  --red:#e3161f;
  --red-dark:#b3080f;
  --green:#7bc02a;
  --ink:#222222;
  --dark:#262626;
  --dark-card:#333333;
  --grey-text:#8a8a8a;
  --white:#ffffff;
  --footer:#232323;
}
*{margin:0;padding:0;box-sizing:border-box}
html,body{width:1200px;height:3874px;overflow:hidden}
body{position:relative;background:var(--white);font-family:'Montserrat',sans-serif;color:var(--ink)}
.btn{position:absolute;display:inline-block;background:var(--red);color:var(--white);font-family:'Lobster',cursive;font-size:15px;line-height:30px;height:30px;padding:0 16px;border-radius:15px;text-decoration:none;white-space:nowrap}

/* hero */
.hero{position:absolute;left:0;top:0;width:1200px;height:600px;background:linear-gradient(90deg,#1a0606 0%,#3a0a0c 35%,#5a0f12 60%,#2a0708 100%);overflow:hidden}
.hero-curtain{position:absolute;inset:0;background:repeating-linear-gradient(90deg,rgba(0,0,0,.25) 0 22px,rgba(255,255,255,0) 22px 48px)}
.hero-art{position:absolute;left:600px;top:0;width:600px;height:600px;background:radial-gradient(circle at 45% 40%,#f3cf5a 0%,#d99a2b 30%,#b3161c 58%,rgba(90,15,18,0) 78%)}
.brand{position:absolute;left:93px;top:26px;font-family:'Bebas Neue',sans-serif;font-size:40px;letter-spacing:1px;color:var(--red);display:flex;align-items:center;gap:8px}
.brand .dot{width:14px;height:14px;border-radius:50%;background:var(--red)}
.menu-toggle{position:absolute;left:1029px;top:28px;display:flex;align-items:center;gap:10px;color:var(--white);font-size:12px;font-weight:600}
.menu-toggle .bars{width:32px;height:16px;display:flex;flex-direction:column;justify-content:space-between}
.menu-toggle .bars i{display:block;height:2px;background:var(--white)}
.hero-kicker{position:absolute;left:94px;top:176px;font-family:'Bebas Neue',sans-serif;font-size:44px;color:var(--white);letter-spacing:.5px}
.hero-kicker .r{color:var(--red)}.hero-kicker .g{color:var(--green)}
.hero-title{position:absolute;left:94px;top:214px;font-family:'Montserrat',sans-serif;font-weight:900;font-style:italic;font-size:100px;letter-spacing:4px;color:var(--white);line-height:110px}
.hero-title .g{color:var(--green)}
.hero-text{position:absolute;left:94px;top:324px;width:460px;font-size:14px;line-height:22px;color:var(--white);font-weight:500}
.offer{position:absolute;left:272px;top:490px;display:flex}
.offer-red{width:230px;height:110px;background:var(--red);color:var(--white);font-family:'Bebas Neue',sans-serif;padding:14px 0 0 40px}
.offer-red .s{font-size:30px;line-height:28px;display:block}
.offer-red .o{font-size:60px;line-height:58px;display:block}
.offer-green{width:130px;height:110px;background:var(--green);color:var(--white);font-family:'Bebas Neue',sans-serif;text-align:center;padding-top:20px}
.offer-green .n{font-size:46px;line-height:44px}
.offer-green .n small{font-size:22px}
.offer-green .off{display:block;font-size:24px;line-height:24px}

/* occasion cards */
.occasions{position:absolute;left:93px;top:684px;display:flex;gap:14px}
.occ{position:relative;width:328px;height:221px;background:var(--white);box-shadow:0 2px 10px rgba(0,0,0,.15);overflow:hidden}
.occ h3{position:absolute;left:34px;top:42px;font-family:'Prata',serif;font-weight:400;font-size:42px;line-height:52px;color:var(--ink);z-index:2;white-space:nowrap}
.occ .sub{position:absolute;left:34px;top:92px;font-family:'Lobster',cursive;font-size:20px;color:var(--red);z-index:2}
.occ .pic{position:absolute;right:0;top:0;width:140px;height:221px;background:radial-gradient(circle at 50% 55%,#e9b85c 0%,#c7352a 45%,rgba(255,255,255,0) 72%)}
.occ .band{position:absolute;left:0;bottom:0;width:188px;height:44px;background:var(--red)}
.occ .more{position:absolute;left:32px;bottom:12px;font-family:'Lobster',cursive;font-size:15px;color:var(--white);text-decoration:underline;z-index:2}

/* menu dark */
.menu-sec{position:absolute;left:0;top:990px;width:1200px;height:595px;background:var(--dark)}
.sec-title{position:absolute;left:0;width:1200px;text-align:center;font-family:'Prata',serif;font-size:54px;font-weight:400}
.sec-title .g{color:var(--green)}
.cards{position:absolute;left:93px;display:flex;gap:14px}
.card{position:relative;width:244px;height:360px;text-align:center}
.card .pic{position:absolute;left:14px;top:15px;width:216px;height:200px}
.card h4{position:absolute;left:0;right:0;top:223px;font-family:'Prata',serif;font-weight:400;font-size:20px}
.card p{position:absolute;left:14px;right:14px;top:258px;font-size:10.5px;line-height:16px;color:var(--grey-text)}
.card .btn{left:50%;transform:translateX(-50%);top:305px;padding:0 18px}
.menu-sec .card{background:var(--dark-card)}
.menu-sec .card h4{color:var(--green)}
.arrow{position:absolute;width:36px;height:36px;border-radius:50%;display:flex;align-items:center;justify-content:center;font-size:14px}
.menu-sec .arrow{background:#3b3b3b;color:#bbb}

/* about */
.about-pic{position:absolute;left:45px;top:1712px;width:515px;height:336px;background:radial-gradient(ellipse at 50% 40%,#fbeccb 0%,#efd9a7 30%,#2f8aa3 55%,rgba(255,255,255,0) 75%)}
.eyebrow{position:absolute;font-family:'Prata',serif;font-size:30px;font-weight:400}
.big{position:absolute;font-family:'Prata',serif;font-size:52px;font-weight:400;white-space:nowrap}
.copy{position:absolute;font-size:13.5px;line-height:22px;color:var(--grey-text)}

/* boozy */
.boozy{position:absolute;left:0;top:2137px;width:1200px;height:405px;background:linear-gradient(90deg,#5f6369 0%,#52565c 50%,#2f3236 100%);overflow:hidden}
.boozy-pic{position:absolute;left:620px;top:0;width:580px;height:405px;background:radial-gradient(circle at 55% 50%,#e6a34a 0%,#b86b2a 22%,#2b2c30 50%,rgba(43,44,48,0) 80%)}
.boozy .eyebrow,.boozy .big{color:var(--white)}
.boozy .copy{color:#e4e4e4}

/* special */
.special .card{background:var(--white);box-shadow:0 2px 10px rgba(0,0,0,.12)}
.special .card h4{color:var(--ink)}
.special-arrow{background:#f1f1f1;color:#777;box-shadow:0 1px 4px rgba(0,0,0,.15)}

/* video + promo */
.video{position:absolute;left:93px;top:3139px;width:497px;height:290px;background:linear-gradient(135deg,#4a4a4a,#2a2220 55%,#5a3a30);overflow:hidden}
.video-tag{position:absolute;left:130px;top:122px;font-family:'Montserrat',sans-serif;font-weight:900;font-size:38px;color:var(--white);letter-spacing:1px}
.video-side{position:absolute;right:20px;top:40px;display:flex;flex-direction:column;gap:8px}
.video-side i{display:block;width:26px;height:26px;background:rgba(0,0,0,.6);border-radius:3px}
.video-bar{position:absolute;left:18px;right:20px;bottom:16px;height:32px;background:rgba(0,0,0,.65);display:flex;align-items:center;padding:0 14px;gap:14px}
.video-bar .play{width:14px;height:14px;border-left:4px solid #fff;border-right:4px solid #fff}
.video-bar .track{flex:1;height:6px;background:#555;position:relative}
.video-bar .track b{position:absolute;left:0;top:0;height:6px;width:48%;background:#999}
.video-bar .hd{font-size:13px;font-weight:900;font-style:italic;color:#4ea0ff}
.promo{position:absolute;left:612px;top:3139px;width:494px;height:290px;border-radius:10px;background:linear-gradient(135deg,#0e5aa8,#1d86d6);overflow:hidden}
.promo-pic{position:absolute;left:240px;top:40px;width:250px;height:240px;background:radial-gradient(circle at 55% 55%,#e8312a 0%,#d2231f 28%,#f4cf2a 42%,rgba(255,255,255,.85) 55%,rgba(29,134,214,0) 75%)}
.promo .script{position:absolute;left:28px;top:40px;font-family:'Lobster',cursive;font-size:24px;color:var(--white)}
.promo h3{position:absolute;left:28px;top:70px;font-family:'Prata',serif;font-weight:400;font-size:42px;line-height:48px;color:var(--white)}
.promo p{position:absolute;left:28px;top:172px;width:200px;font-size:12px;line-height:17px;color:#e4f0fb}
.promo .btn{left:30px;top:216px;font-size:14px;height:26px;line-height:26px}

/* footer */
.footer{position:absolute;left:0;top:3512px;width:1200px;height:362px;background:var(--footer);color:#cfcfcf}
.footer h5{position:absolute;top:44px;font-family:'Lobster',cursive;font-weight:400;font-size:22px;color:var(--white)}
.footer ul{position:absolute;top:88px;list-style:none;font-size:12px}
.footer li{height:31.6px}
.contact-row{position:absolute;display:flex;gap:8px;font-size:12px;line-height:17px}
.contact-row svg{flex:none;margin-top:2px}
.field{position:absolute;left:854px;width:252px;height:26px;background:var(--white);color:#555;font-size:10px;line-height:26px;padding-left:10px}
.subscribe{position:absolute;left:854px;top:153px;width:252px;height:27px;background:var(--red);color:var(--white);font-size:11px;font-weight:600;text-align:center;line-height:27px}
.socials{position:absolute;left:854px;top:200px;display:flex;gap:8px}
.socials i{display:block;width:24px;height:24px;border-radius:50%;border:1px solid #777}
.foot-brand{position:absolute;left:0;width:1200px;top:246px;text-align:center;font-family:'Bebas Neue',sans-serif;font-size:32px;color:var(--red);letter-spacing:1px}
.copyright{position:absolute;left:0;width:1200px;top:308px;text-align:center;font-size:11px;color:#cfcfcf}
.copyright span{color:var(--red)}
</style>
</head>
<body>

<header class="hero">
  <div class="hero-curtain"></div>
  <div class="hero-art" role="img" aria-label="Popcorn bursting from a striped red bucket with 3D glasses and a cinema ticket"></div>
  <div class="brand"><span class="dot"></span>Pop Parlor</div>
  <div class="menu-toggle">MENU <span class="bars"><i></i><i></i><i></i></span></div>
  <div class="hero-kicker"><span class="r">POPCORN</span> BOWL <span class="g">&amp;</span></div>
  <h1 class="hero-title">SN<span class="g">A</span>CKS</h1>
  <p class="hero-text">Sed ut perspiciatis unde omnis iste natus error sit voluptatem accusantium</p>
  <a class="btn" style="left:94px;top:384px;height:28px;line-height:28px;font-size:14px">More Details</a>
  <div class="offer">
    <div class="offer-red"><span class="s">SPECIAL</span><span class="o">OFFER</span></div>
    <div class="offer-green"><span class="n">80<small> %</small></span><span class="off">OFF</span></div>
  </div>
</header>

<section class="occasions">
  <article class="occ">
    <div class="pic" role="img" aria-label="Red striped cup and popcorn box for kids"></div>
    <h3>Gifts</h3><span class="sub">For Kids</span>
    <div class="band"></div>
    <span class="more">Read More</span>
  </article>
  <article class="occ">
    <div class="pic" role="img" aria-label="Chocolate shake being poured into a glass"></div>
    <h3>Thank You</h3><span class="sub">Popcorn</span>
    <div class="band"></div>
    <span class="more">Read More</span>
  </article>
  <article class="occ">
    <div class="pic" role="img" aria-label="Ice cream sundae with sprinkles in a cup"></div>
    <h3>Birthday</h3><span class="sub">Popcorn</span>
    <div class="band"></div>
    <span class="more">Read More</span>
  </article>
</section>

<section class="menu-sec">
  <h2 class="sec-title" style="top:62px;color:#fff">Our <span class="g">Menu</span></h2>
  <span class="arrow" style="left:29px;top:312px">‹</span>
  <span class="arrow" style="left:1135px;top:312px">›</span>
  <div class="cards" style="top:151px">
    <div class="card"><div class="pic" role="img" aria-label="Gourmet popcorn in a red bucket" style="background:linear-gradient(180deg,#f2e4bd,#d02a22 60%,#7a0f10)"></div><h4>Gourmet Popcorn</h4><p>Sed ut perspiciatis unde omnis iste natus error sit voluptatem...</p><a class="btn">Read More</a></div>
    <div class="card"><div class="pic" role="img" aria-label="Pink strawberry shake with straw" style="background:linear-gradient(180deg,#2d3a35,#e9a8c0 55%,#3e4f55)"></div><h4>Fancy Shakes</h4><p>Sed ut perspiciatis unde omnis iste natus error sit voluptatem...</p><a class="btn">Read More</a></div>
    <div class="card"><div class="pic" role="img" aria-label="Berry ice cream in a glass with strawberries" style="background:radial-gradient(circle at 50% 40%,#b5506a,#3a2a2a 55%,#1e1a1a)"></div><h4>Ice Cream</h4><p>Sed ut perspiciatis unde omnis iste natus error sit voluptatem...</p><a class="btn">Read More</a></div>
    <div class="card"><div class="pic" role="img" aria-label="Popcorn tins" style="background:radial-gradient(circle at 45% 55%,#f2d33a,#7fb34a 40%,#5a5a5a 75%)"></div><h4>Popcorn Tins</h4><p>Sed ut perspiciatis unde omnis iste natus error sit voluptatem...</p><a class="btn">Read More</a></div>
  </div>
</section>

<section>
  <div class="about-pic" role="img" aria-label="Blue bowl overflowing with popcorn"></div>
  <span class="eyebrow" style="left:600px;top:1670px">About</span>
  <h2 class="big" style="left:600px;top:1704px">Pop Parlor</h2>
  <p class="copy" style="left:600px;top:1778px;width:510px">But I must explain to you how all this mistaken idea of denouncing pleasure and praising pain was born and I will give you a complete account of the system, and expound the actual teachings of the great explorer of the truth, the master-builder of human happiness. No one rejects, dislikes, or avoids pleasure itself, because it is pleasure, but because those who do not know how to pursue pleasure rationally encounter consequences that are extremely painful.</p>
  <p class="copy" style="left:600px;top:1940px;width:510px">But I must explain to you how all this mistaken idea of denouncing pleasure and praising pain was born and I will give you a complete account of the system, and expound the actual teachings...</p>
  <a class="btn" style="left:600px;top:2025px">Read More</a>
</section>

<section class="boozy">
  <div class="boozy-pic" role="img" aria-label="Whipped cream topped shake with cinnamon sticks and cookies on dark slate"></div>
  <span class="eyebrow" style="left:96px;top:52px">Fancy</span>
  <h2 class="big" style="left:96px;top:86px">Boozy Shakes</h2>
  <p class="copy" style="left:96px;top:154px;width:495px">But I must explain to you how all this mistaken idea of denouncing pleasure and praising pain was born and I will give you a complete account of the system, and expound the actual teachings of the great explorer of the truth, the master-builder of human happiness. No one rejects, dislikes, or avoids pleasure itself, because it is pleasure, but because those who do not know how to pursue pleasure rationally encounter consequences that are extremely painful.</p>
  <a class="btn" style="left:97px;top:334px">Read More</a>
</section>

<section class="special">
  <h2 class="sec-title" style="top:2610px">Special <span class="g">Menu</span></h2>
  <span class="arrow special-arrow" style="left:29px;top:2855px">‹</span>
  <span class="arrow special-arrow" style="left:1135px;top:2855px">›</span>
  <div class="cards" style="top:2694px">
    <div class="card"><div class="pic" role="img" aria-label="Popcorn in a wooden bowl" style="background:linear-gradient(180deg,#ececec,#f1dfae 50%,#b98a5a)"></div><h4>Popcorn</h4><p>Sed ut perspiciatis unde omnis iste natus error sit voluptatem...</p><a class="btn">Read More</a></div>
    <div class="card"><div class="pic" role="img" aria-label="Two chocolate boozy shakes with cream" style="background:linear-gradient(180deg,#f4f4f4,#c9a489 45%,#6e4430)"></div><h4>Boozy Shakes</h4><p>Sed ut perspiciatis unde omnis iste natus error sit voluptatem...</p><a class="btn">Read More</a></div>
    <div class="card"><div class="pic" role="img" aria-label="Child holding a green gift bag" style="background:linear-gradient(180deg,#f0a534,#e58f1f 55%,#c6d63a)"></div><h4>Gift Bag</h4><p>Sed ut perspiciatis unde omnis iste natus error sit voluptatem...</p><a class="btn">Read More</a></div>
    <div class="card"><div class="pic" role="img" aria-label="Colourful ice cream scoops in cones" style="background:linear-gradient(180deg,#f3f3f3,#9ad6c9 45%,#e8738a 70%,#f2f2f2)"></div><h4>Ice Cream</h4><p>Sed ut perspiciatis unde omnis iste natus error sit voluptatem...</p><a class="btn">Read More</a></div>
  </div>
</section>

<div class="video" role="img" aria-label="Promotional video of a shake being enjoyed">
  <span class="video-tag">&amp; SHAKES</span>
  <div class="video-side"><i></i><i></i><i></i><i></i></div>
  <div class="video-bar"><span class="play"></span><span style="font-size:9px;color:#fff">00:08</span><span class="track"><b></b></span><span class="hd">HD</span></div>
</div>
<div class="promo">
  <div class="promo-pic" role="img" aria-label="Red gift box with sale tag, up to 70% off"></div>
  <span class="script">Special</span>
  <h3>Gift<br>Promotion</h3>
  <p>Sed ut perspiciatis unde omnis iste natus error...</p>
  <a class="btn">Promotion Now</a>
</div>

<footer class="footer">
  <h5 style="left:95px">Quick Links</h5>
  <ul style="left:95px"><li>Home</li><li>About Us</li><li>Menu</li><li>Gift/Promotion</li><li>Contact Us</li></ul>
  <h5 style="left:347px">Menu</h5>
  <ul style="left:347px"><li>Popcorn</li><li>Ice Cream</li><li>Popcorn tin</li><li>Fancy Shakes</li><li>Gift Bag</li></ul>
  <h5 style="left:567px">Contact Us</h5>
  <div class="contact-row" style="left:567px;top:88px;width:200px">
    <svg width="10" height="13" viewBox="0 0 10 13"><path d="M5 0a5 5 0 0 1 5 5c0 3-5 8-5 8S0 8 0 5a5 5 0 0 1 5-5z" fill="#7bc02a"/><circle cx="5" cy="5" r="2" fill="#232323"/></svg>
    <span>42 Kernel Lane<br>Maple Falls 30 USA</span></div>
  <div class="contact-row" style="left:567px;top:148px">
    <svg width="11" height="11" viewBox="0 0 11 11"><path d="M2 0l2 2.5-1.2 1.5a6 6 0 0 0 4 4L8.5 6.8 11 9l-1.5 2C4 11 0 7 0 1.5z" fill="#7bc02a"/></svg>
    <span>+1 (555) 204 7731</span></div>
  <div class="contact-row" style="left:567px;top:190px">
    <svg width="12" height="9" viewBox="0 0 12 9"><rect width="12" height="9" fill="#7bc02a"/><path d="M0 0l6 5 6-5" stroke="#232323" fill="none"/></svg>
    <span>rt@fizzlane.net</span></div>
  <h5 style="left:856px">Newsletter</h5>
  <div class="field" style="top:86px">Enter Name:</div>
  <div class="field" style="top:120px">Enter Email:</div>
  <div class="subscribe">Subscribe</div>
  <div class="socials"><i></i><i></i><i></i></div>
  <div class="foot-brand">Pop Parlor</div>
  <p class="copyright">Copyright © 2019 <span>Pop Parlor</span>. All rights reserved.</p>
</footer>

</body>
</html>
```